Moodvane - Landing Page

Need a landing page for a journal app. The app is based on a retrospective board, where each journal entry is split into 3 sections: "What went well", "What Didn't Go Well" and "Things To Try".
The landing page should match the style of all modern web application landing pages. Think Plumo, Vexora, Zenquil. I've included screenshots of the app.
One feature that I want to highlight that is not ready yet, is an AI coach. It will offer insights based on the history of the user's journal entries
1 page

```html
<!DOCTYPE html>
<html lang="en">
<head>
<meta charset="utf-8">
<title>Moodvane – Transform Your Journaling Experience</title>
<link href="https://fonts.googleapis.com/css2?family=Poppins:wght@400;500;600;700&family=Inter:wght@400;500;600;700&display=swap" rel="stylesheet">
<style>
:root{
  --ink:#1f2329;
  --muted:#4a5260;
  --brand:#0d4ea6;
  --blue:#1565c0;
  --sky:#dde9f5;
  --mist:#f3f6f9;
  --haze:#e6eef7;
  --dark:#23272d;
  --foot:#2b2d31;
  --green:#2eb872;
  --amber:#f5b700;
  --white:#fff;
}
*{box-sizing:border-box;margin:0;padding:0}
html,body{width:1200px;height:3215px;overflow:hidden}
body{position:relative;font-family:"Inter",sans-serif;color:var(--ink);background:var(--white)}
.abs{position:absolute}
.head{font-family:"Poppins",sans-serif}

/* hero */
.hero{left:0;top:0;width:1200px;height:562px;background:var(--sky)}
.logo{display:flex;align-items:center;gap:10px;font-family:"Poppins",sans-serif;font-weight:700;font-size:21px;color:var(--ink)}
.logo .dot{width:20px;height:20px;border-radius:50%;background:var(--amber)}
.nav{left:462px;top:20px;display:flex;gap:22px;font-size:14px;color:var(--ink)}
.btn-outline{left:985px;top:13px;width:110px;height:34px;border:1.5px solid var(--brand);border-radius:17px;color:var(--brand);font-size:11px;display:flex;align-items:center;justify-content:center}
.eyebrow{left:103px;top:162px;font-size:23px;font-family:"Poppins",sans-serif}
.hero-title{left:103px;top:200px;font-family:"Poppins",sans-serif;font-weight:700;font-size:42px;line-height:52px}
.hero-title .hl{color:var(--brand)}
.hero-copy{left:103px;top:378px;width:330px;font-size:15px;line-height:18px;color:var(--ink)}
.btn-dark{left:103px;top:453px;width:221px;height:50px;border-radius:25px;background:var(--dark);color:#fff;font-size:14px;font-weight:600;display:flex;align-items:center;justify-content:center;gap:10px}
.hero-photo{left:538px;top:135px;width:562px;height:427px;border-radius:60px 30px 0 90px;background:linear-gradient(135deg,#e9c9a4 0%,#c0743a 45%,#eef0f2 70%,#f7f7f7 100%)}
.icon-panel{left:527px;top:200px;width:155px;height:116px;border-radius:16px;background:rgba(150,185,225,.75)}
.badge-c{width:62px;height:62px;border-radius:50%;border:4px solid rgba(255,255,255,.7)}

/* stats */
.stats{left:0;top:562px;width:1200px;height:71px;background:var(--dark);display:flex;justify-content:center;align-items:center}
.stat{display:flex;align-items:center;gap:12px;color:#fff;font-size:11px;font-weight:700;padding:0 32px;border-right:1px solid #444a52}
.stat:last-child{border:none}
.stat i{width:26px;height:26px;border-radius:50%;border:3px solid #7aa4d6;display:block}

/* why */
.h2{font-family:"Poppins",sans-serif;font-weight:500;font-size:46px;text-align:center;width:1200px;left:0}
.lead{left:195px;width:810px;text-align:center;font-size:11.5px;line-height:17.5px;color:var(--ink)}
.feat{width:142px;font-size:11.5px;line-height:17.5px;color:var(--muted)}
.feat h3{font-size:15px;font-weight:700;line-height:18px;color:var(--ink);margin-bottom:8px}
.feat.r{text-align:right}
.check{width:30px;height:30px}
.app{background:#fff;border:2px solid #cfe0f2;border-radius:8px;overflow:hidden;box-shadow:0 10px 30px rgba(20,60,110,.1)}
.app .bar{height:16px;background:#f1f3f6;display:flex;gap:5px;align-items:center;padding-left:8px}
.app .bar i{width:6px;height:6px;border-radius:50%;display:block}
.side{position:absolute;left:0;top:16px;bottom:0;width:18px;background:var(--dark)}
.col{position:absolute;top:65px;width:105px;height:185px;border:1px solid #e4e7ec;border-radius:3px;background:#fafbfc;padding:6px}
.col b{font-size:5px;font-weight:600;display:block;margin-bottom:10px}
.col .ln{height:3px;background:#d6dbe2;border-radius:2px;margin:4px 0}

/* how */
.how{left:0;top:1196px;width:1200px;height:571px;background:linear-gradient(135deg,#0f4d9c,#1a66bd 50%,#0e4f9f)}
.how-panel{left:62px;top:1240px;width:1076px;height:490px;background:rgba(255,255,255,.07);border-radius:4px}
.how-title{left:190px;top:1430px;font-family:"Poppins",sans-serif;font-weight:500;font-size:46px;line-height:52px;color:#fff}
.step{background:#fff;width:210px;height:140px;padding:16px 15px;font-size:11.5px;line-height:17.5px;color:var(--muted)}
.step h4{color:var(--blue);font-size:14px;font-weight:700;margin:6px 0}
.step .ic{width:26px;height:22px;border-radius:4px}
.num{width:34px;height:34px;border-radius:50%;background:var(--dark);border:3px solid #d9e2ee;color:#fff;font-weight:700;font-size:14px;display:flex;align-items:center;justify-content:center}

/* ai coach */
.coach{left:0;top:1767px;width:1200px;height:623px;background:var(--mist)}
.avatar{border-radius:50%}
.pill{height:32px;border-radius:16px;background:#fff;box-shadow:0 6px 18px rgba(0,0,0,.08);display:flex;align-items:center;font-size:12px;color:#9aa3ae;gap:8px;padding:0 12px}
.pill b{background:var(--blue);color:#fff;font-weight:500;font-size:11px;border-radius:12px;padding:5px 10px}

/* testimonials */
.voices{left:0;top:2390px;width:1200px;height:545px;background:var(--haze)}
.quote{left:772px;top:2666px;width:239px;height:180px;background:var(--blue);border-radius:14px;color:#fff;padding:20px;font-size:10px;line-height:16px;box-shadow:0 16px 30px rgba(21,101,192,.3)}
.quote h5{font-size:15px;font-weight:600;margin-top:8px}
.stars{display:flex;align-items:center;gap:3px;font-size:8px;margin-top:6px}
.stars i{width:9px;height:9px;background:var(--amber);display:block;clip-path:polygon(50% 0,61% 35%,98% 35%,68% 57%,79% 91%,50% 70%,21% 91%,32% 57%,2% 35%,39% 35%)}

/* footer */
.footer{left:0;top:2935px;width:1200px;height:280px;background:var(--foot);color:#c9ced6;font-size:11.5px}
.footer .logo{color:#fff}
.fl{line-height:29px}
.fl h6{font-size:13px;color:#fff;font-weight:600;margin-bottom:8px}
.store{width:74px;height:24px;border:1px solid #9aa0a8;border-radius:4px;background:#111}
.soc{width:8px;height:8px;border-radius:50%;background:#c9ced6}
.legal{font-size:10px;color:#9ba2ad}
</style>
</head>
<body>

<section class="hero abs"></section>
<div class="logo abs" style="left:105px;top:20px"><span class="dot"></span>Moodvane</div>
<nav class="nav abs"><span>Demo</span><span>/</span><span>Community</span><span>/</span><span>Pricing</span><span>/</span><span>Enterprise</span></nav>
<a class="btn-outline abs">Contact Sales</a>

<p class="eyebrow abs">From Reflection to Action:</p>
<h1 class="hero-title abs"><span class="hl">Transform</span> Your<br>Journaling<br><span class="hl">Experience</span></h1>
<p class="hero-copy abs">Organize your thoughts, track your progress, and gain insights with a journal designed for personal growth</p>
<a class="btn-dark abs">Start Your Journey
  <svg width="16" height="12" viewBox="0 0 16 12"><path d="M1 6h13M9 1l5 5-5 5" stroke="#fff" stroke-width="1.6" fill="none"/></svg></a>

<div class="hero-photo abs" role="img" aria-label="Cheerful man holding an open laptop over a desk with notes"></div>
<div class="icon-panel abs"></div>
<div class="badge-c abs" style="left:553px;top:232px;background:#f59e1b"></div>
<div class="badge-c abs" style="left:646px;top:232px;background:#1c6fc0"></div>
<div class="badge-c abs" style="left:740px;top:232px;background:#35b46a"></div>

<div class="stats abs">
  <div class="stat"><i></i>24/7 Support</div>
  <div class="stat"><i></i>Weekly Updates</div>
  <div class="stat"><i></i>Secure and Compliant</div>
  <div class="stat"><i></i>99.9% Uptime</div>
</div>

<h2 class="h2 abs" style="top:698px">Why Choose Us?</h2>
<p class="lead abs" style="top:779px"><b>Discover</b> a journaling experience tailored to help you grow. Our app's <b>unique retrospective</b> board format encourages thoughtful reflection, while the upcoming AI coach provides personalized insights to guide your journey. With a user-friendly design and powerful tracking features, our app makes it easy to stay <b>organized</b>, <b>focused</b>, and <b>committed</b> to your personal development.</p>

<div class="feat r abs" style="left:166px;top:877px"><h3>Retrospective<br>Board Format</h3>Reflect on your experiences with our unique three-part journal structure.</div>
<div class="feat r abs" style="left:166px;top:1020px"><h3>AI-Powered<br>Insights</h3>Get personalized insights based on your journal history with our upcoming AI coach.</div>
<div class="feat abs" style="left:887px;top:904px"><h3>Track Progress</h3>Monitor your growth over time with easy-to-read summaries.</div>
<div class="feat abs" style="left:887px;top:1011px;width:130px"><h3>User-Friendly<br>Design</h3>Enjoy a clean, intuitive interface that makes journaling a breeze.</div>

<svg class="check abs" style="left:340px;top:918px" viewBox="0 0 30 30"><circle cx="15" cy="15" r="15" fill="var(--green)"/><path d="M8 15l5 5 9-10" stroke="#fff" stroke-width="3" fill="none"/></svg>
<svg class="check abs" style="left:340px;top:1060px" viewBox="0 0 30 30"><circle cx="15" cy="15" r="15" fill="var(--green)"/><path d="M8 15l5 5 9-10" stroke="#fff" stroke-width="3" fill="none"/></svg>
<svg class="check abs" style="left:825px;top:925px" viewBox="0 0 30 30"><circle cx="15" cy="15" r="15" fill="var(--green)"/><path d="M8 15l5 5 9-10" stroke="#fff" stroke-width="3" fill="none"/></svg>
<svg class="check abs" style="left:825px;top:1043px" viewBox="0 0 30 30"><circle cx="15" cy="15" r="15" fill="var(--green)"/><path d="M8 15l5 5 9-10" stroke="#fff" stroke-width="3" fill="none"/></svg>

<div class="app abs" style="left:392px;top:875px;width:410px;height:260px">
  <div class="bar"><i style="background:#f25f58"></i><i style="background:#f9be2e"></i><i style="background:#3ac84a"></i></div>
  <div class="side"></div>
  <div class="abs" style="left:38px;top:30px;font-size:7px;font-weight:700">Entry</div>
  <div class="abs" style="left:38px;top:44px;width:50px;height:3px;background:#d6dbe2"></div>
  <div class="abs" style="left:95px;top:42px;width:16px;height:7px;border-radius:4px;background:var(--green)"></div>
  <div class="col" style="left:40px"><b>What Went Well?</b><div class="ln"></div><div class="ln" style="width:80%"></div><div class="ln"></div><div class="ln" style="width:70%"></div><div class="ln"></div></div>
  <div class="col" style="left:162px"><b>What Didn't Go Well?</b><div class="ln"></div><div class="ln" style="width:75%"></div><div class="ln"></div><div class="ln" style="width:85%"></div><div class="ln" style="width:60%"></div></div>
  <div class="col" style="left:283px"><b>Things To Try</b><div class="ln"></div><div class="ln" style="width:80%"></div><div class="ln"></div><div class="ln"></div><div class="ln" style="width:70%"></div><div class="ln"></div></div>
</div>

<section class="how abs"></section>
<div class="how-panel abs"></div>
<h2 class="how-title abs">How Does it<br>Work?</h2>

<div class="step abs" style="left:801px;top:1288px"><div class="ic" style="background:#3d7fd1"></div><h4>Start Journaling</h4>Create entries by reflecting on what went well, what didn't, and what to try next.</div>
<div class="step abs" style="left:540px;top:1406px;text-align:right"><div class="ic" style="background:var(--amber);margin-left:auto"></div><h4 style="text-align:center">Organize Your Thoughts</h4>Keep your ideas and reflections organized in a clear, structured format.</div>
<div class="step abs" style="left:801px;top:1542px"><div class="ic" style="background:#f2c23a;width:22px;border-radius:50%"></div><h4>Unlock Insights</h4>Soon, our AI coach will provide you with valuable feedback and tips based on your entries.</div>

<svg class="abs" style="left:0;top:0" width="1200" height="1700" viewBox="0 0 1200 1700">
  <g stroke="#fff" stroke-dasharray="2 3" fill="none" opacity=".85">
    <path d="M912 1430v33q0 12-12 12H795"/>
    <path d="M638 1548v34q0 12 12 12H758"/>
  </g>
  <circle cx="857" cy="1475" r="6" fill="#fff"/><path d="M859 1472l-4 3 4 3z" fill="var(--blue)"/>
  <circle cx="692" cy="1594" r="6" fill="#fff"/><path d="M690 1591l4 3-4 3z" fill="var(--blue)"/>
</svg>

<div class="num abs" style="left:758px;top:1340px">1</div>
<div class="num abs" style="left:758px;top:1458px">2</div>
<div class="num abs" style="left:758px;top:1594px">3</div>

<section class="coach abs"></section>
<h2 class="h2 abs" style="top:1863px">Your Personal AI Coach</h2>
<p class="lead abs" style="top:1943px;left:190px;width:820px">Briefly explain the upcoming feature. Get ready for the next level of journaling with our AI Coach, coming soon! This smart feature will analyze your journal entries to offer personalized insights, tips, and recommendations. Whether you're reflecting on past experiences or planning future goals, the AI Coach will be your guide, helping you grow faster and more effectively.</p>

<div class="app abs" style="left:387px;top:2023px;width:426px;height:270px;border-color:#d7dde5">
  <div class="bar"><i style="background:#f25f58"></i><i style="background:#f9be2e"></i><i style="background:#3ac84a"></i></div>
  <div class="side"></div>
  <div class="abs" style="left:40px;top:32px;height:11px;padding:0 6px;background:var(--blue);color:#fff;font-size:5px;line-height:11px;border-radius:2px">+ Create Project</div>
  <div class="abs" style="left:40px;top:72px;width:58px;height:56px;border:1px solid #e6e9ee;border-radius:3px;font-size:5px;padding:40px 4px 0">Default Journal</div>
  <div class="abs" style="left:132px;top:72px;width:58px;height:56px;border:1px solid #e6e9ee;border-radius:3px;font-size:5px;padding:40px 4px 0">Gym</div>
  <div class="abs" style="left:224px;top:72px;width:58px;height:56px;border:1px solid #e6e9ee;border-radius:3px;font-size:5px;padding:40px 4px 0">Personal</div>
  <div class="abs" style="left:316px;top:72px;width:58px;height:56px;border:1px solid #e6e9ee;border-radius:3px;font-size:5px;padding:40px 4px 0">Work</div>
</div>

<div class="avatar abs" style="left:738px;top:2031px;width:148px;height:148px;background:#fff;box-shadow:0 10px 30px rgba(0,0,0,.1)"></div>
<div class="avatar abs" style="left:750px;top:2043px;width:124px;height:124px;background:linear-gradient(160deg,#f7c23a,#e08a1a)" role="img" aria-label="Portrait of the male AI coach avatar in a suit"></div>
<div class="pill abs" style="left:843px;top:2091px"><b>Kai</b>Your AI Coach</div>

<div class="avatar abs" style="left:324px;top:2144px;width:148px;height:148px;background:#fff;box-shadow:0 10px 30px rgba(0,0,0,.1)"></div>
<div class="avatar abs" style="left:336px;top:2156px;width:124px;height:124px;background:linear-gradient(160deg,#5fd3a0,#1e9d6a)" role="img" aria-label="Portrait of the female AI coach avatar in a blazer"></div>
<div class="pill abs" style="left:247px;top:2201px">Your AI Coach<b>Ivo</b></div>

<section class="voices abs"></section>
<div class="avatar abs" style="left:204px;top:2500px;width:62px;height:62px;background:#f2b02a" role="img" aria-label="Smiling user portrait"></div>
<div class="avatar abs" style="left:313px;top:2524px;width:76px;height:76px;background:#d8c6b8" role="img" aria-label="User portrait"></div>
<div class="avatar abs" style="left:476px;top:2499px;width:62px;height:62px;background:#cfa88e" role="img" aria-label="User portrait"></div>
<div class="avatar abs" style="left:665px;top:2483px;width:64px;height:64px;background:#9ca7b1" role="img" aria-label="User portrait"></div>
<div class="avatar abs" style="left:938px;top:2478px;width:72px;height:72px;background:#9aa89a" role="img" aria-label="User portrait"></div>
<div class="avatar abs" style="left:188px;top:2620px;width:78px;height:78px;background:#b59a82" role="img" aria-label="User portrait"></div>
<div class="avatar abs" style="left:280px;top:2723px;width:62px;height:62px;background:#5a86b8" role="img" aria-label="User portrait"></div>
<div class="avatar abs" style="left:750px;top:2510px;width:170px;height:170px;background:rgba(120,165,220,.18)"></div>
<div class="avatar abs" style="left:770px;top:2530px;width:130px;height:130px;background:rgba(120,165,220,.3)"></div>
<div class="avatar abs" style="left:780px;top:2540px;width:110px;height:110px;background:#4a86cf;border:6px solid #6d9edb" role="img" aria-label="Portrait of the featured reviewer"></div>

<h2 class="head abs" style="left:360px;width:410px;top:2590px;text-align:center;font-weight:500;font-size:46px;line-height:55px">What Our Users<br>Are Saying</h2>
<p class="abs" style="left:370px;width:390px;top:2715px;text-align:center;font-size:14.5px;line-height:17px">See now our members have reduced stress and enhanced wel-being with our support and guidance.</p>

<div class="quote abs">
  The team was fast, professional, and took care of everything! They cleared out my garage in no time, and I couldn't be happier with how smooth the process was. Highly recommend!
  <h5>Nora P</h5>
  <div style="font-size:9px;opacity:.7">Marketing</div>
  <div class="stars"><i></i><i></i><i></i><i></i><i></i><span style="margin-left:8px">4.8 out of 5.0</span></div>
</div>

<footer class="footer abs">
  <div class="logo abs" style="left:189px;top:52px"><span class="dot"></span>Moodvane</div>
  <p class="abs" style="left:189px;top:92px;width:220px;line-height:17.5px">Our journal app helps you reflect, grow, and stay organized with a unique retrospective board format.</p>
  <div class="abs" style="left:189px;top:171px;font-size:10px;color:#9ba2ad">Language <b style="color:#fff;margin:0 10px 0 6px">ENG</b>
    <svg width="10" height="6" viewBox="0 0 10 6"><path d="M1 1l4 4 4-4" stroke="#fff" fill="none" stroke-width="1.4"/></svg></div>

  <div class="fl abs" style="left:503px;top:48px"><h6>Links</h6>About Us<br>Contact Us<br>Enterprise<br>Contact Sales</div>
  <div class="fl abs" style="left:617px;top:85px">Integrations<br>Pricing<br>Template<br>24/7 Support</div>

  <div class="fl abs" style="left:797px;top:48px"><h6>Download</h6></div>
  <div class="store abs" style="left:797px;top:87px"></div>
  <div class="store abs" style="left:883px;top:87px"></div>
  <div class="abs" style="left:797px;top:135px;display:flex;align-items:center;gap:10px"><span class="soc" style="width:10px;height:10px"></span>Accessbility Statement</div>
  <div class="abs" style="left:797px;top:176px;display:flex;gap:19px">
    <span class="soc"></span><span class="soc"></span><span class="soc"></span><span class="soc"></span><span class="soc"></span>
  </div>

  <div class="legal abs" style="left:189px;top:240px">Terms &amp; Conditions &nbsp;&nbsp;|&nbsp;&nbsp; Privacy Policy &nbsp;&nbsp;|&nbsp;&nbsp; Refund Policy</div>
  <div class="legal abs" style="left:800px;top:240px">© 2024 —Moodvane.app. All Rights Reserved.</div>
</footer>

</body>
</html>
```